Maple Crest Dental

This is not a full design. I have an almost completed design of the home page. This project is just to modify one page (home page) of an app only. The colors and logos are already designed. The file attached "Homepage_1" is the home page. I need a high resolution of this design with the same color with the following changes:
1. The 4 icons for "floss reminder", "Check-up and cleaning Reminder", "Schedule Appointment", and "Contact Your Dentist" options should be re-designed. I am looking for similar silhouettes with the same color, but more professional looking.
-The floss icon is simple enough, just a floss.
-The check-up reminder should be some dental tools.
-Schedule Appointment should be a calendar, I have attached similar designs.
-Contact your dentist should be a silhouette of a healthcare provider.
All four designs are silhouettes with the same color as they are in the attached home page.
These are the main changes. The following are other minor adjustments:
-The logo on top should be slightly lowered. The address right under it should be modified with the same font as the logo and be placed better in relation to the phone and mail icons under it. I have attached an EPS and a PNG file of our logo.
-The separating lines between the different options should be thinner.
-The picture of the user on the top right should be larger
-The setting icon on the top left should have three lines of equal lengths
Once again, this is only modifying an existing design of only one page for a phone app.

```html
<!DOCTYPE html>
<html lang="en">
<head>
<meta charset="utf-8">
<title>Maple Crest Dental – Home</title>
<link href="https://fonts.googleapis.com/css2?family=Roboto:wght@300;400;500&display=swap" rel="stylesheet">
<style>
  :root {
    --stage-center: #0b6b9c;
    --stage-edge: #073653;
    --header-blue: #006aa0;
    --row-blue: #9dd9ea;
    --ink-blue: #0c6499;
    --divider-blue: #10608f;
    --icon-soft: #8fd0e4;
    --white: #ffffff;
    --url-yellow: #f2e830;
  }
  * { box-sizing: border-box; margin: 0; padding: 0; }
  html, body { width: 1200px; height: 1000px; overflow: hidden; }
  body {
    position: relative;
    font-family: "Roboto", Arial, sans-serif;
    background: radial-gradient(ellipse 620px 560px at 720px 560px, var(--stage-center), var(--stage-edge));
  }

  .app-screen {
    position: absolute;
    left: 181px; top: 51px;
    width: 492px; height: 872px;
    background: var(--row-blue);
    box-shadow: 0 6px 24px rgba(0, 20, 40, 0.55);
  }

  .app-header {
    position: absolute; left: 0; top: 0;
    width: 492px; height: 164px;
    background: var(--header-blue);
  }
  .brand {
    position: absolute; left: 0; top: 50px; width: 492px;
    display: flex; justify-content: center; align-items: center; gap: 8px;
    color: var(--white); font-weight: 300; font-size: 17px; letter-spacing: 0.5px;
  }
  .brand-dot { width: 10px; height: 10px; border-radius: 50%; background: var(--white); }
  .menu-button { position: absolute; left: 15px; top: 117px; }
  .contact-icons { position: absolute; left: 190px; top: 117px; }
  .user-photo {
    position: absolute; left: 397px; top: 61px;
    width: 83px; height: 77px;
    background: linear-gradient(135deg, #6a4a3e, #2a2a33 55%, #8a3a2a);
  }
  .user-name {
    position: absolute; left: 387px; top: 142px; width: 103px;
    text-align: center; color: var(--white); font-size: 9px;
  }

  .menu-row {
    position: absolute; left: 0; width: 492px;
    border-bottom: 2px solid var(--divider-blue);
  }
  .row-floss { top: 164px; height: 173px; }
  .row-checkup { top: 337px; height: 180px; }
  .row-appointment { top: 517px; height: 176px; }
  .row-dentist { top: 693px; height: 179px; border-bottom-width: 2px; }

  .row-icon {
    position: absolute; left: 15px;
    background: var(--ink-blue); opacity: 0.85; border-radius: 6px;
  }
  .row-floss .row-icon { top: 45px; width: 94px; height: 80px; }
  .row-checkup .row-icon { top: 54px; width: 74px; height: 86px; }
  .row-appointment .row-icon { top: 52px; width: 87px; height: 72px; }
  .row-dentist .row-icon { top: 34px; width: 81px; height: 102px; }

  .row-label {
    position: absolute; left: 120px; width: 250px; top: 50%;
    transform: translateY(-50%);
    text-align: center; color: var(--ink-blue);
    font-weight: 500; font-size: 19.5px; line-height: 26px;
  }
  .row-arrow { position: absolute; left: 445px; top: 50%; transform: translateY(-50%); }

  .presentation-note {
    position: absolute; left: 750px; top: 322px;
    color: var(--white); font-weight: 300; font-size: 33px; line-height: 52px;
  }
  .presentation-url {
    position: absolute; left: 749px; top: 440px;
    color: var(--url-yellow); font-size: 20px; font-weight: 400;
  }
</style>
</head>
<body>
  <main class="app-screen">
    <header class="app-header">
      <div class="brand"><span class="brand-dot"></span><span class="brand-name">MAPLE CREST DENTAL</span></div>

      <svg class="menu-button" width="36" height="24" viewBox="0 0 36 24" aria-label="Menu">
        <g fill="var(--row-blue)">
          <circle cx="3" cy="3" r="3"/><circle cx="3" cy="12" r="3"/><circle cx="3" cy="21" r="3"/>
          <rect x="8" y="0.5" width="28" height="5" rx="2.5"/>
          <rect x="8" y="9.5" width="28" height="5" rx="2.5"/>
          <rect x="8" y="18.5" width="28" height="5" rx="2.5"/>
        </g>
      </svg>

      <svg class="contact-icons" width="104" height="32" viewBox="0 0 104 32" aria-label="Call or email">
        <path fill="var(--row-blue)" d="M4 28c-3-3-1-7 1-8l4-2c2-1 3 0 4 1l2 2c4-2 7-6 9-10l-2-2c-1-1-2-2-1-4l2-4c1-2 5-3 8 0 1 10-7 27-27 27z" transform="translate(2,0)"/>
        <rect x="47" y="2" width="1" height="28" fill="#3f8fbf"/>
        <rect x="64" y="5" width="37" height="24" rx="1" fill="var(--row-blue)"/>
        <path d="M64 6l18.5 13L101 6" fill="none" stroke="var(--header-blue)" stroke-width="2"/>
        <path d="M64 28l13-11M101 28L88 17" fill="none" stroke="var(--header-blue)" stroke-width="1.5"/>
      </svg>

      <div class="user-photo" role="img" aria-label="Profile photo of the signed-in user"></div>
      <div class="user-name">Dana Whitlow</div>
    </header>

    <section class="menu-row row-floss">
      <div class="row-icon" role="img" aria-label="Dental floss dispenser icon"></div>
      <div class="row-label">Floss Reminder</div>
      <svg class="row-arrow" width="20" height="34" viewBox="0 0 20 34"><path d="M0 0L20 17L0 34z" fill="var(--ink-blue)"/></svg>
    </section>

    <section class="menu-row row-checkup">
      <div class="row-icon" role="img" aria-label="Dental tools icon"></div>
      <div class="row-label">Check-up and Cleaning<br>Reminder</div>
      <svg class="row-arrow" width="20" height="34" viewBox="0 0 20 34"><path d="M0 0L20 17L0 34z" fill="var(--ink-blue)"/></svg>
    </section>

    <section class="menu-row row-appointment">
      <div class="row-icon" role="img" aria-label="Calendar with stopwatch icon"></div>
      <div class="row-label">Schedule Appointment</div>
      <svg class="row-arrow" width="20" height="34" viewBox="0 0 20 34"><path d="M0 0L20 17L0 34z" fill="var(--ink-blue)"/></svg>
    </section>

    <section class="menu-row row-dentist">
      <div class="row-icon" role="img" aria-label="Healthcare provider silhouette icon"></div>
      <div class="row-label">Contact Your Dentist</div>
      <svg class="row-arrow" width="20" height="34" viewBox="0 0 20 34"><path d="M0 0L20 17L0 34z" fill="var(--ink-blue)"/></svg>
    </section>
  </main>

  <p class="presentation-note">For real size mock up,<br>please visit below URL:</p>
  <p class="presentation-url">www.northpixelstudio.com/HomeScreen.png</p>
</body>
</html>
```